Business Cards Needed

Hi designers, I have a new logo that was created by one of the PixelHarbor designers. I'd now like to use that logo to make business cards. The company is called CarewiseMetrics Advisory and is a business consulting firm. I'd like the business cards to be horizontal, modern, and professional.
I'd like the following information to be on the business card:
1) Logo
2) my name - Janine Oulton
3) my title - Principal
4) name of business - CarewiseMetrics Advisory
5) mobile - 508.742.3391
6) e-mail - janine@carewisemetricsadvisory.example
I'm uploading a JPG file of the logo. I'm hoping this is the correct file format. Please let me know if you need another type of file. Thank you.

```html
<!DOCTYPE html>
<html lang="en">
<head>
<meta charset="utf-8">
<title>CarewiseMetrics Advisory – Business Card</title>
<link rel="stylesheet" href="https://fonts.googleapis.com/css2?family=Montserrat:wght@500;600;700&display=swap">
<style>
  :root {
    --brand-blue: #1c76bc;
    --brand-green: #8fc13e;
    --card-white: #ffffff;
    --backdrop: #959595;
    --text-font: "Montserrat", Arial, sans-serif;
  }
  * { margin: 0; padding: 0; box-sizing: border-box; }
  html, body {
    width: 1200px; height: 1108px; overflow: hidden;
    background: var(--backdrop);
    font-family: var(--text-font);
  }
  .card {
    position: absolute; left: 244px;
    width: 712px; height: 408px;
    border-radius: 30px; overflow: hidden;
  }
  .card--front { top: 120px; background: var(--brand-blue); }
  .card--back { top: 582px; background: var(--card-white); }

  .wordmark {
    position: absolute;
    font-weight: 600; letter-spacing: 0.2px; white-space: nowrap;
  }
  .card--front .wordmark {
    left: 0; right: 0; top: 178px; text-align: center;
    font-size: 40px; color: var(--card-white);
  }
  .card--back .wordmark {
    right: 40px; top: 76px; font-size: 25px; color: var(--brand-blue);
  }

  .wave { position: absolute; left: 0; top: 0; width: 712px; height: 408px; }

  .contact-block {
    position: absolute; left: 30px; top: 222px; color: var(--card-white);
  }
  .contact-block__name { font-size: 27px; font-weight: 700; line-height: 1.1; }
  .contact-block__title { font-size: 17px; font-weight: 600; margin-top: 8px; }
  .contact-list { list-style: none; margin-top: 26px; }
  .contact-list li {
    display: flex; align-items: center; gap: 8px;
    font-size: 18px; font-weight: 500; height: 27px;
  }
  .contact-list svg { width: 17px; height: 17px; fill: var(--brand-green); flex: none; }
</style>
</head>
<body>

<section class="card card--front">
  <div class="wordmark">CarewiseMetrics Advisory</div>
</section>

<section class="card card--back">
  <div class="wordmark">CarewiseMetrics Advisory</div>

  <svg class="wave" viewBox="0 0 712 408" aria-hidden="true">
    <path fill="var(--brand-blue)"
      d="M0,183 C120,128 260,135 420,178 C540,210 630,222 712,180 L712,408 L0,408 Z"/>
    <path fill="var(--brand-green)"
      d="M0,186 C140,140 280,140 420,184 C540,218 630,222 712,178 L712,208 C630,240 540,240 420,212 C280,176 140,160 0,218 Z"/>
    <path fill="var(--brand-green)"
      d="M0,218 C140,160 280,170 420,212 C540,250 620,262 712,226 L712,408 L0,408 Z"/>
    <path fill="var(--card-white)"
      d="M150,152 C290,160 420,205 540,236 C620,252 670,246 712,226 L712,246 C650,272 580,280 520,272 C420,250 300,190 150,152 Z"/>
    <path fill="var(--brand-blue)"
      d="M0,218 C140,160 280,178 420,226 C520,262 600,280 712,244 L712,408 L0,408 Z"/>
  </svg>

  <div class="contact-block">
    <div class="contact-block__name">Janine Oulton</div>
    <div class="contact-block__title">Principal</div>
    <ul class="contact-list">
      <li>
        <svg viewBox="0 0 24 24" aria-hidden="true"><path d="M2 9c0-3 5-5 10-5s10 2 10 5v2h-5V9c-3-1-7-1-10 0v2H2zM6 12h12l3 8H3z"/></svg>
        <span>508.742.3391</span>
      </li>
      <li>
        <svg viewBox="0 0 24 24" aria-hidden="true"><path d="M2 5h20v14H2zM3 6l9 7 9-7v2l-9 7-9-7z" fill-rule="evenodd"/></svg>
        <span>janine@carewisemetricsadvisory.example</span>
      </li>
      <li>
        <svg viewBox="0 0 24 24" aria-hidden="true"><circle cx="12" cy="12" r="10"/></svg>
        <span>www.carewisemetricsadvisory.example</span>
      </li>
    </ul>
  </div>
</section>

</body>
</html>
```